Valtora

Standard Business Card design.
Sample two-sided design uploaded. White front, Black back.
Would like white shield to be on all black background side.
Willing to look at a couple creative designs, but nothing crazy.
Preference for a classic, confident, strong design.

```html
<!DOCTYPE html>
<html lang="en">
<head>
<meta charset="utf-8">
<title>Valtora Business Card</title>
<link href="https://fonts.googleapis.com/css2?family=Montserrat:wght@400;500;700&display=swap" rel="stylesheet">
<style>
  :root {
    --backdrop: #4b4b4b;
    --card: #ffffff;
    --ink: #111111;
    --muted: #2a2a2a;
  }
  * { margin: 0; padding: 0; box-sizing: border-box; }
  html, body { width: 1200px; height: 780px; overflow: hidden; }
  body {
    background: var(--backdrop);
    font-family: "Montserrat", Arial, sans-serif;
    color: var(--ink);
    position: relative;
  }
  .card {
    position: absolute;
    width: 560px;
    height: 320px;
    background: var(--card);
    border-radius: 26px;
    overflow: hidden;
  }
  .card--front { left: 40px; top: 70px; }
  .card--back { left: 600px; top: 390px; }

  .front-brand {
    position: absolute;
    inset: 0;
    display: flex;
    align-items: center;
    justify-content: center;
  }
  .brand-name {
    font-weight: 700;
    text-transform: uppercase;
    color: var(--ink);
  }
  .front-brand .brand-name { font-size: 64px; letter-spacing: 10px; }

  .back-swoosh { position: absolute; inset: 0; }

  .back-brand {
    position: absolute;
    right: 40px;
    top: 62px;
  }
  .back-brand .brand-name { font-size: 34px; letter-spacing: 5px; }

  .address {
    position: absolute;
    right: 40px;
    top: 122px;
    text-align: right;
    font-size: 12px;
    line-height: 1.45;
    color: var(--muted);
  }
  .divider {
    position: absolute;
    left: 150px;
    right: 30px;
    top: 170px;
    height: 1.5px;
    background: var(--ink);
  }
  .person {
    position: absolute;
    left: 150px;
    top: 182px;
  }
  .person__name { font-size: 19px; font-weight: 700; letter-spacing: 0.5px; }
  .person__title { font-size: 12px; color: var(--muted); margin-top: 1px; }
  .person__rule {
    width: 150px;
    height: 1.5px;
    background: var(--ink);
    margin: 8px 0 7px;
  }
  .contacts { list-style: none; }
  .contacts li {
    display: flex;
    align-items: center;
    gap: 8px;
    font-size: 12.5px;
    line-height: 19px;
    color: var(--muted);
  }
  .contacts svg { width: 11px; height: 11px; flex: none; }
</style>
</head>
<body>

  <section class="card card--front">
    <div class="front-brand">
      <span class="brand-name">Valtora</span>
    </div>
  </section>

  <section class="card card--back">
    <svg class="back-swoosh" viewBox="0 0 560 320" aria-hidden="true">
      <path d="M0 0 L335 0 C205 40 112 135 82 320 L0 320 Z" fill="#111"/>
      <path d="M305 12 C195 58 112 150 68 320" fill="none" stroke="#fff" stroke-width="3"/>
    </svg>

    <div class="back-brand"><span class="brand-name">Valtora</span></div>

    <p class="address">Your address, City<br>State, Zip 1234</p>

    <div class="divider"></div>

    <div class="person">
      <h1 class="person__name">MARCUS REED</h1>
      <p class="person__title">Managing Director</p>
      <div class="person__rule"></div>
      <ul class="contacts">
        <li>
          <svg viewBox="0 0 12 12" aria-hidden="true"><path d="M2 1 L4.5 1 L5.5 3.5 L4 4.5 C4.7 6 6 7.3 7.5 8 L8.5 6.5 L11 7.5 L11 10 C11 10.6 10.6 11 10 11 C5 11 1 7 1 2 C1 1.4 1.4 1 2 1 Z" fill="#111"/></svg>
          123 456 789
        </li>
        <li>
          <svg viewBox="0 0 12 12" aria-hidden="true"><rect x="0.5" y="2" width="11" height="8" rx="1" fill="#111"/><path d="M1 2.5 L6 6.5 L11 2.5" fill="none" stroke="#fff" stroke-width="1"/></svg>
          info@yourgmail.com
        </li>
        <li>
          <svg viewBox="0 0 12 12" aria-hidden="true"><circle cx="6" cy="6" r="5.5" fill="#111"/><ellipse cx="6" cy="6" rx="2.3" ry="5.5" fill="none" stroke="#fff" stroke-width="0.8"/><path d="M0.5 6 H11.5" stroke="#fff" stroke-width="0.8"/></svg>
          www.yourwebsite.com
        </li>
      </ul>
    </div>
  </section>

</body>
</html>
```